website for local kavenda practicioner and yoga teacher trainer

The website should function primarily as:
A place where people can discover Kavenda and book sessions.
A central hub connecting all of my work.
A professional home that reflects my personality and approach.
Website design for Liesbet Oonwerk — Kavenda® Structural Integration practitioner, movement educator, yoga teacher and teacher trainer.
A website that can grow with future projects.
The website should feel: Warm, Human, Invitational, Professional, Accessible, Intelligent, Calm, Clear, Playful, Exploratory, Trustworthy
Avoid: New age aesthetics, Mystical clichés, Excessive spirituality, ”Guru" vibes, Overly clinical design, Corporate wellness branding, Busy layouts
Think: modern, grounded, curious and real.
My work combines three interconnected areas:
1.Bodywork: Touch, structure, awareness and one-on-one support.
2. Movement: Yoga, Pilates and embodied movement.
3. Education: Teacher trainings, workshops and continued learning.
Underlying values:
Curiosity over certainty
Possibility over perfection
Complexity without overwhelm
Science and lived experience together
Exploration rather than dogma
Human beings before methods
The primary goal of the website is to introduce people to Kavenda® Structural Integration and make it easy for them to:
Understand what Kavenda is
Discover whether it might be relevant for them
Learn what to expect from a session
Book an appointment
Booking should always feel visible and easy.
Secondary Goal: Present all other aspects of my work in one coherent place:
Yoga classes
Pilates classes
Teacher trainings
Workshops
Retreats
One-on-one movement sessions
Collaborations with studios
Website Structure
1: HOME
1.1.Hero Section: Large welcoming image
1.2 Two Main Pathways
- Bodywork: Kavenda® Structural Integration
- Movement & Education: Yoga, Pilates, trainings, workshops and retreats
- About Preview: Small introduction with portrait. + Button:
Read More
1.3 Current Events / What's Coming Up: Upcoming trainings, workshops and retreats. (This section should be easy to update)
1.4. Contact / Newsletter: Simple contact information
2: Kavenda® Structural Integration
What is Kavenda?
For whom is it?
What does a session look like?
FAQ
Prices
Booking
Future possibility:
Kaven Movement sessions
3: Movement
- Introductory text.
- Studio Classes (link to “my home base” - > local yoga studio)
- One-to-One Sessions: booking option (this is small; not a key aspect I want to promote)
- Workshops/ Retreats / Teacher Trainings => This section should be flexible and easy to update. Visitors should be able to click into specific offerings.
4. Events
Dynamic page for: Teacher trainings, Retreats, Workshops (see section in movement; here more elaborate)
Each event should contain: Image, Short description, Location, Date, Button for more information. (Linking to hosting studio/location)
5. Work With Me
For studios, organisations and teacher training schools.
Examples: Guest teaching, Workshops, Anatomy, Sequencing, Teacher development , Continuing education -> Clear call-to-action.
Call to action!!=> Book a Session
Prominent button in the navigation.
Footer:
- About Me: Longer biography (6th page)
Personal story and background.
- Testimonials (7th page): Separate page containing testimonials from:
Kavenda clients
Students
Teacher trainees
- Contact: 8th page
Visual Direction
Natural textures. Lots of white space.Editorial feeling.Professional photography.Simple navigation.
Less "wellness influencer.” More:Thoughtful, Contemporary, Timeless, Grounded, Human
Photography should show:
Teaching
Hands-on work
Natural movement
Real interaction
Simplicity
Avoid stereotypical yoga imagery and overly spiritual aesthetics.
Keywords
Warm. Curious. Human. Professional. Embodied. Intelligent. Accessible. Playful. Grounded. Exploratory. Real.
Inspiration / Core Message
Helping people feel more at home in their bodies through touch, movement and education.
The website should communicate that these are not separate services, but different expressions of the same intention:
Bodywork • Movement • Education.
Colours:
light orange/beige: e3d5c4
light orange/off white: f9f7f3
gray azure: 556b78
orange: d07b5a
grey orange: c09f80
dark grey: 3e3e3e
dark gray cyan 2f4f4f
gray green colour: a7c4a0
Fonts: Montserrat and Poppins + raleway
In added documents a try out idea of a website + logo. I will mainly use the logo with diffrent colours (image next to text).
My audience consists of people who want to feel more at home in their bodies and who appreciate a thoughtful, grounded and human approach to movement, touch and education. (30-65yo)
wellbeing
5+ page
- montserrat, poppins, raleway

```html
<!DOCTYPE html>
<html lang="en">
<head>
<meta charset="utf-8">
<title>Liesbet Oonwerk — Bodywork · Movement · Education</title>
<link href="https://fonts.googleapis.com/css2?family=Montserrat:wght@400;500;600&family=Poppins:ital,wght@0,300;0,400;0,500;1,300&family=Raleway:wght@400;500&display=swap" rel="stylesheet">
<style>
:root{
  --sand:#e3d5c4;
  --offwhite:#f9f7f3;
  --band:#f4f2ee;
  --blush:#f4ebe4;
  --azure:#556b78;
  --orange:#d07b5a;
  --greyorange:#c09f80;
  --darkgrey:#3e3e3e;
  --ink:#2f4f4f;
  --sage:#a7c4a0;
  --line:#e6e0d8;
}
*{box-sizing:border-box;margin:0;padding:0}
html,body{width:1200px;height:4456px;overflow:hidden;background:#fff}
body{font-family:'Poppins',sans-serif;color:var(--darkgrey);position:relative}
.abs{position:absolute}
.eyebrow{font-family:'Montserrat',sans-serif;font-size:12px;letter-spacing:3px;text-transform:uppercase;color:var(--orange);font-weight:500}
.heading{font-family:'Poppins',sans-serif;font-weight:300;color:var(--ink);letter-spacing:-.5px}
.body-text{font-size:13px;line-height:1.75;color:var(--darkgrey)}
.text-link{font-family:'Montserrat',sans-serif;font-size:12px;letter-spacing:2px;text-transform:uppercase;color:var(--ink);font-weight:600;border-bottom:1px solid var(--orange);padding-bottom:4px;text-decoration:none;display:inline-block}
.btn{display:inline-block;font-family:'Montserrat',sans-serif;font-size:12px;letter-spacing:1.5px;text-transform:uppercase;font-weight:500;border-radius:22px;padding:0 20px;height:42px;line-height:42px;text-decoration:none}
.btn-solid{background:var(--orange);color:#fff}
.btn-outline{border:1.5px solid var(--ink);color:var(--ink);line-height:39px}
.photo{border-radius:2px}
.logo{display:flex;align-items:center;gap:10px;font-family:'Poppins',sans-serif;font-size:18px;color:var(--ink);font-weight:400}
.logo-dot{width:22px;height:22px;border-radius:50%;background:var(--orange)}

/* nav */
.site-nav{left:0;top:0;width:1200px;height:64px}
.site-nav .logo{position:absolute;left:65px;top:18px}
.nav-links{position:absolute;left:350px;top:22px;display:flex;gap:42px;font-family:'Montserrat',sans-serif;font-size:13px;letter-spacing:1px;color:var(--ink)}
.nav-links .active{color:var(--orange)}
.site-nav .btn{position:absolute;left:972px;top:10px}

/* hero */
.hero-title{left:65px;top:186px;font-size:62px;line-height:71px}
.hero-title em{font-style:normal;color:var(--orange)}
.hero-shape{left:800px;top:104px;width:260px;height:390px}
.hero-lede{left:711px;top:368px;width:425px;font-size:13px;line-height:1.6;color:var(--darkgrey)}

/* pathways */
.center{text-align:center;left:0;width:1200px}
.card-label{font-family:'Montserrat',sans-serif;font-size:12px;letter-spacing:2px;color:var(--orange);text-transform:uppercase}
.card-title{font-size:26px;font-weight:300;color:var(--ink)}
.event-title{font-size:18px;font-weight:400;color:var(--ink)}
.event-meta{font-size:11px;color:var(--greyorange)}
.event-desc{font-size:12px;line-height:1.55;color:var(--darkgrey)}

.about-band{left:0;top:1881px;width:1200px;height:669px;background:var(--band)}
.quote-band{left:0;top:3492px;width:1200px;height:265px;background:var(--blush)}
.quote{font-family:'Poppins',sans-serif;font-style:italic;font-weight:300;font-size:23px;line-height:35px;color:var(--azure)}

.input{border:1px solid var(--line);border-radius:22px;background:var(--offwhite);height:42px;line-height:40px;padding:0 20px;font-size:12px;color:#aaa}

.footer-head{font-family:'Montserrat',sans-serif;font-size:12px;letter-spacing:1px;color:var(--orange);text-transform:uppercase;font-weight:500}
.footer-list{list-style:none;font-size:12px;line-height:25px;color:var(--darkgrey)}
.social{font-family:'Montserrat',sans-serif;font-size:10px;letter-spacing:2px;color:var(--azure);text-transform:uppercase}
.rule{left:65px;top:4414px;width:1070px;height:1px;background:var(--line)}
.small{font-size:12px;color:var(--darkgrey)}
</style>
</head>
<body>

<header class="abs site-nav">
  <div class="logo"><span class="logo-dot"></span>Liesbet Oonwerk</div>
  <nav class="nav-links"><span class="active">Home</span><span>Kavenda®</span><span>Movement</span><span>Events</span><span>Work With Me</span></nav>
  <a class="btn btn-solid" href="#">Book a session</a>
</header>

<section>
  <p class="abs eyebrow" style="left:65px;top:148px">Bodywork · Movement · Education</p>
  <h1 class="abs heading hero-title">Helping people feel<br><em>more at home</em> in<br>their bodies.</h1>
  <a class="abs btn btn-solid" style="left:65px;top:437px;height:44px;line-height:44px" href="#">Book a session</a>
  <a class="abs btn btn-outline" style="left:252px;top:437px;height:44px" href="#">Discover Kavenda®</a>
  <svg class="abs hero-shape" viewBox="0 0 260 390" aria-hidden="true">
    <circle cx="140" cy="200" r="130" fill="#f4ebe4" opacity=".7"/>
  </svg>
  <p class="abs hero-lede">Through touch, movement and education, I support people in exploring their bodies with curiosity, awareness and possibility.</p>
  <div class="abs photo" role="img" aria-label="Sunlit treatment room with a wooden massage table and a plant by the window" style="left:65px;top:545px;width:653px;height:449px;background:linear-gradient(135deg,#f0c48c,#d89a5a 60%,#b5733d)"></div>
  <div class="abs photo" role="img" aria-label="Close-up of hands resting on a cream cushion in warm light" style="left:738px;top:545px;width:396px;height:449px;background:linear-gradient(160deg,#9a5a2c,#d89c68 55%,#f1dcc0)"></div>
</section>

<section>
  <p class="abs eyebrow center" style="top:1087px">Two pathways</p>
  <h2 class="abs heading center" style="top:1118px;font-size:35px;line-height:54px">Different expressions of the same intention —<br>helping you meet your body with care and clarity.</h2>

  <div class="abs photo" role="img" aria-label="Hands-on bodywork with hands resting on a cushion" style="left:65px;top:1257px;width:521px;height:333px;background:linear-gradient(160deg,#9a5a2c,#d89c68 55%,#f1dcc0)"></div>
  <p class="abs card-label" style="left:65px;top:1624px">01 — Bodywork</p>
  <h3 class="abs card-title" style="left:65px;top:1650px">Kavenda® Structural Integration</h3>
  <p class="abs body-text" style="left:65px;top:1697px;width:520px">Touch, structure, awareness and one-on-one support. A series of sessions that work with fascia and movement to reshape how you live in your body.</p>
  <a class="abs text-link" style="left:65px;top:1770px" href="#">Explore Kavenda →</a>

  <div class="abs photo" role="img" aria-label="Movement teacher balancing on one leg on a mat in a bright studio" style="left:614px;top:1257px;width:520px;height:333px;background:linear-gradient(180deg,#e9e2da,#cfc2b4 60%,#8a5434)"></div>
  <p class="abs card-label" style="left:614px;top:1624px">02 — Practice</p>
  <h3 class="abs card-title" style="left:614px;top:1650px">Movement &amp; Education</h3>
  <p class="abs body-text" style="left:614px;top:1697px;width:500px">Yoga, Pilates, workshops, teacher trainings and embodied learning — for anyone curious about how the body moves, organises and rests.</p>
  <a class="abs text-link" style="left:614px;top:1770px" href="#">Explore movement →</a>
</section>

<section>
  <div class="abs about-band"></div>
  <div class="abs photo" role="img" aria-label="Portrait of the practitioner sitting cross-legged beside a laptop and a plant" style="left:71px;top:1964px;width:519px;height:502px;background:linear-gradient(120deg,#e6e0d6,#c7a98a 55%,#8f6a48)"></div>
  <p class="abs eyebrow" style="left:628px;top:1980px">About Liesbet</p>
  <h2 class="abs heading" style="left:628px;top:2017px;font-size:36px;line-height:52px;width:520px">A thoughtful expert helping people feel more at home in their bodies.</h2>
  <p class="abs body-text" style="left:628px;top:2192px;width:500px;line-height:27px">I'm a Kavenda® Structural Integration practitioner, movement educator, yoga teacher and teacher trainer. My work lives at the meeting point of science and lived experience — structure and awareness, movement and curiosity.</p>
  <p class="abs body-text" style="left:628px;top:2325px;width:500px;line-height:27px">For more than a decade I've been guiding individuals and teachers in exploring the body as a living, intelligent, ever-changing landscape — not something to fix, but somewhere to belong.</p>
  <a class="abs text-link" style="left:628px;top:2430px" href="#">Read more</a>
</section>

<section>
  <p class="abs eyebrow" style="left:68px;top:2650px">Upcoming</p>
  <h2 class="abs heading" style="left:68px;top:2675px;font-size:50px;line-height:52px">Workshops, trainings &amp;<br>moments to gather.</h2>
  <a class="abs text-link" style="left:1004px;top:2764px" href="#">All events →</a>

  <div class="abs photo" role="img" aria-label="Group of movement teachers practising together in a studio" style="left:65px;top:2830px;width:340px;height:330px;background:linear-gradient(180deg,#ece7e0,#b9a28c 60%,#7e563a)"></div>
  <p class="abs card-label" style="left:65px;top:3185px;font-size:11px">Teacher training</p>
  <h3 class="abs event-title" style="left:65px;top:3207px">Anatomy for Movement Teachers</h3>
  <p class="abs event-meta" style="left:65px;top:3244px">14 — 16 March 2026 · Antwerp, BE</p>
  <p class="abs event-desc" style="left:65px;top:3272px;width:340px">A three-day immersion for yoga and Pilates teachers exploring functional anatomy as a living, breathing inquiry.</p>
  <a class="abs text-link" style="left:65px;top:3347px;font-size:11px" href="#">Learn more →</a>

  <div class="abs photo" role="img" aria-label="Movement teacher in a standing balance on a mat" style="left:429px;top:2830px;width:340px;height:330px;background:linear-gradient(180deg,#e9e2da,#cfc2b4 60%,#8a5434)"></div>
  <p class="abs card-label" style="left:429px;top:3185px;font-size:11px">Retreat</p>
  <h3 class="abs event-title" style="left:429px;top:3207px">Spring Movement Retreat</h3>
  <p class="abs event-meta" style="left:429px;top:3244px">9 — 12 May 2026 · Provence, FR</p>
  <p class="abs event-desc" style="left:429px;top:3272px;width:340px">Four slow days of practice, hands-on bodywork and quiet exploration in a converted farmhouse.</p>
  <a class="abs text-link" style="left:429px;top:3328px;font-size:11px" href="#">Learn more →</a>

  <div class="abs photo" role="img" aria-label="Close-up of hands on a cushion during a fascia workshop" style="left:794px;top:2830px;width:340px;height:330px;background:linear-gradient(160deg,#9a5a2c,#d89c68 55%,#f1dcc0)"></div>
  <p class="abs card-label" style="left:794px;top:3185px;font-size:11px">Workshop</p>
  <h3 class="abs event-title" style="left:794px;top:3207px">Fascia &amp; Felt-Sense Workshop</h3>
  <p class="abs event-meta" style="left:794px;top:3244px">21 June 2026 · Online</p>
  <p class="abs event-desc" style="left:794px;top:3272px;width:340px">An afternoon of lecture and embodied practice — meeting the connective tissue from the inside out.</p>
  <a class="abs text-link" style="left:794px;top:3328px;font-size:11px" href="#">Learn more →</a>
</section>

<section>
  <div class="abs quote-band"></div>
  <blockquote class="abs quote center" style="top:3572px">“Liesbet's work is quietly profound. I left every session<br>knowing my body a little better than when I arrived.”</blockquote>
  <p class="abs eyebrow center" style="top:3661px;font-size:10px;color:var(--greyorange)">— C. R., Kavenda client</p>
</section>

<section>
  <p class="abs eyebrow" style="left:78px;top:3836px">Stay connected</p>
  <h2 class="abs heading" style="left:78px;top:3870px;font-size:48px;line-height:50px">A few thoughtful notes<br>a year — on the body,<br>movement and what's<br>next.</h2>
  <div class="abs input" style="left:653px;top:4027px;width:294px">Your email address</div>
  <a class="abs btn btn-solid" style="left:958px;top:4027px;font-size:11px" href="#">Subscribe</a>
</section>

<footer>
  <div class="abs logo" style="left:65px;top:4200px"><span class="logo-dot"></span>Liesbet Oonwerk</div>
  <p class="abs small" style="left:65px;top:4240px;width:260px;line-height:19px">Kavenda® Structural Integration, movement and education — supporting people in feeling more at home in their bodies.</p>
  <div class="abs input" style="left:65px;top:4335px;width:155px;height:40px;line-height:38px;font-size:11px">Your email</div>
  <a class="abs btn btn-solid" style="left:226px;top:4335px;height:40px;line-height:40px;font-size:11px;padding:0 22px" href="#">Stay connected</a>

  <p class="abs footer-head" style="left:456px;top:4185px">Explore</p>
  <ul class="abs footer-list" style="left:456px;top:4208px"><li>Kavenda®</li><li>Movement</li><li>Events</li><li>Work With Me</li></ul>
  <p class="abs footer-head" style="left:681px;top:4185px">About</p>
  <ul class="abs footer-list" style="left:681px;top:4208px"><li>About Liesbet</li><li>Testimonials</li><li>Contact</li></ul>
  <p class="abs footer-head" style="left:906px;top:4185px">Studio</p>
  <p class="abs small" style="left:906px;top:4210px;line-height:19px">Antwerp, Belgium<br>hello@liesbetoonwerk.be</p>
  <p class="abs social" style="left:906px;top:4265px">Photo Feed &nbsp; Work Profile &nbsp; Newsletter</p>

  <div class="abs rule"></div>
  <p class="abs small" style="left:65px;top:4430px;font-size:11px">© 2026 Liesbet Oonwerk. All rights reserved.</p>
  <p class="abs social" style="left:836px;top:4431px;font-size:11px;width:300px;text-align:right">Bodywork · Movement · Education</p>
</footer>

</body>
</html>
```